依頼詳細
新サービスの情報を視覚的にわかりやすく、ワクワクするような形で紹介するチラシの作成を希望しています。

チラシの内容は下記の通りです
<チラシ(表)>
こだま×海外 の
ポコリナクラスが新しくなります!!
「サブスク×専用アプリ」でもっとソトの世界をシルチャンスを!

〇3つの魅力
・サブスク型サービスだから多様なコンテンツに参加し放題!
→コンテンツ一覧は裏面へ
・アプリを活用し、よりわかりやすく、より簡単にアクセスを!
→アプリのダウンロードはこちらから
・兄弟や卒業生、こだまグループ会員外も参加可能に!
→料金詳細は裏面へ

☆(下部に説明会情報を記載)
説明会開催決定!!
▶説明会「ポコリナクラス サービス概要説明会」
3月〇日 / 〇日 開催決定!!
日時:
オンライン開催:
申込はコチラ
※演者紹介も入れる

◆表面は文字情報を少なめに、写真を使い様々な国や料理、文化を視覚的に魅せる

<チラシ(裏)>
◎コンテンツ一覧
12種類のコンテンツ(画像付き)
対象学年・開催曜日
※一部コンテンツはサブスク会員外も単発申込可能(詳細はアプリ内でご確認ください。)
▶ふわっとポコリナ
毎週(月)(水)(金)更新 ポコリナの問題を1問配信
▶星空便り
毎週(火)(木)更新 世界各地の日記を配信

◎「宿泊型企画」ラクダクラス
ポコリナクラスの終着点!
2022年開催時の様子を紹介!(写真数枚にコメントを入れる形、8枚程用意予定)

◎料金説明
表形式で紹介
①サブスク非会員
申込ごとに参加費が発生
(1部イベントのみ申込可能)
コンテンツにより異なる(1回2000~3000円程)
不可

②サブスク会員
※こだまグループ非会員
月額支払いで参加し放題
月額5,500円
原則不可
※こだまグループ入会費13,200(税込)を支払えば参加可能

③サブスク会員
※こだまグループ会員
月額支払いで参加し放題
月額5,500円
可能
※こだまグループ卒業生は卒業後もポコリナサブスク会員である限り可能

記載項目
社名/問い合わせ先/HPURL
サイズ
A4
ページ数
両面
希望イメージ
シンプル 複雑
単色 カラフル
暗い 明るい
日常 高級
遊び心 厳粛
未来的 伝統的
女性的 男性的
希望する色
カラフルなイメージだと嬉しいです!
納品ファイル
• 高解像度JPG (.jpg)
• イラストレーター形式 (.ai)
• PNG形式 (.png)
補足説明
参考のためこれまで配付したチラシを添付しています。
また現在修正中ですがHP(https://kodama-net.jp/pokorina/)もご確認ください。
使用する写真をいくつか添付します(すべて使用するというわけではありません)
また宿泊企画は来週開催なので、開催し次第写真を共有し入れ込んでいただければと思います。

カラフルかつワクワクできる。
これまでのポコリナにない雰囲気も感じられたため。

みなさま本当にありがとうございました!
どのチラシもこれから使用していきたいようなワクワクに溢れていました!

```html
<!DOCTYPE html>
<html lang="ja">
<head>
<meta charset="utf-8">
<title>こだま×海外のポコリナクラスが新しくなります！</title>
<link href="https://fonts.googleapis.com/css2?family=M+PLUS+Rounded+1c:wght@500;700;800&display=swap" rel="stylesheet">
<style>
  :root{
    --stripe-a:#fff6b8;
    --stripe-b:#ffffff;
    --title:#1f6c78;
    --accent-blue:#1596b8;
    --panel:#e6f6fb;
    --panel-edge:#8fd4ea;
    --plane:#bfe6f3;
    --pink:#ec5f8d;
    --pink-soft:#fde7ef;
    --green:#4ba847;
    --ink:#3a3a3a;
    --white:#ffffff;
  }
  *{box-sizing:border-box;margin:0;padding:0}
  html,body{width:849px;height:1200px;overflow:hidden}
  body{font-family:"M PLUS Rounded 1c",sans-serif;color:var(--ink)}
  .flyer{
    position:relative;width:849px;height:1200px;overflow:hidden;
    background:repeating-linear-gradient(135deg,var(--stripe-a) 0 34px,var(--stripe-b) 34px 68px);
  }
  .photo{position:absolute;border-radius:50%;border:6px solid var(--white);box-shadow:0 3px 8px rgba(0,0,0,.12)}
  .photo--abbey{left:-10px;top:10px;width:200px;height:200px;background:linear-gradient(180deg,#5d80c4,#d7a36c 70%,#6a7f5a)}
  .photo--buddha{left:690px;top:40px;width:165px;height:165px;background:radial-gradient(circle at 50% 45%,#9e8a6a,#4f5a3a 75%)}
  .photo--trulli{left:0;top:232px;width:205px;height:205px;background:linear-gradient(180deg,#d98b6c,#e9c9a0 55%,#7f7a64)}
  .photo--cathedral{left:625px;top:330px;width:230px;height:230px;background:linear-gradient(180deg,#7fa2c9,#3d3b48 60%,#2a2a33)}
  .photo--taj{left:-6px;top:448px;width:215px;height:215px;background:linear-gradient(180deg,#e58b5a,#f2c58a 50%,#c9b7a6)}
  .photo--temple{left:665px;top:490px;width:195px;height:195px;background:linear-gradient(180deg,#b9cfe0,#8c7a62 60%,#5f5545)}
  .photo--host{left:680px;top:1012px;width:160px;height:160px;background:radial-gradient(circle at 50% 40%,#d8c2a8,#6f8a9a 70%)}

  .headline{position:absolute;left:250px;top:55px;width:580px;color:var(--title);font-weight:800}
  .headline__lead{font-size:40px;margin-left:100px;letter-spacing:2px}
  .headline__lead small{font-size:30px}
  .headline__brand{display:flex;align-items:flex-end;margin-top:4px}
  .brand-mark{width:96px;height:96px;border-radius:50%;background:var(--title);flex:none;margin-right:14px;margin-top:-60px;align-self:flex-start}
  .headline__name{font-size:54px;letter-spacing:2px;line-height:1.1}
  .headline__name small{font-size:36px;margin-left:6px}
  .headline__news{font-size:42px;margin-left:110px;margin-top:2px;letter-spacing:2px}

  .plane-band{position:absolute;left:120px;top:300px;width:640px;height:90px;background:var(--plane);transform:rotate(16deg);border-radius:45px;opacity:.85}
  .hero-panel{position:absolute;left:228px;top:260px;width:394px;height:305px;background:var(--panel);border:3px dashed var(--panel-edge);text-align:center;padding-top:34px;color:var(--accent-blue)}
  .hero-panel__main{font-size:60px;font-weight:800;line-height:1.05;letter-spacing:2px}
  .hero-panel__cross{font-size:44px;font-weight:800;line-height:1.1}
  .hero-panel__sub{margin-top:18px;font-size:30px;font-weight:800;color:var(--title);line-height:1.45}

  .charm-label{position:absolute;left:30px;top:672px;width:150px;height:40px;border-radius:20px;background:var(--pink-soft);border:3px solid var(--pink);color:var(--pink);font-size:24px;font-weight:800;text-align:center;line-height:34px}
  .charms{position:absolute;left:28px;top:716px;width:795px;display:flex;gap:14px}
  .charm{position:relative;flex:1;height:220px;border-left:3px solid var(--pink);padding:10px 10px 0 74px}
  .charm__num{position:absolute;left:8px;top:0;font-size:96px;font-weight:800;color:var(--white);-webkit-text-stroke:3px var(--pink);line-height:1}
  .charm__text{font-size:16px;font-weight:700;line-height:1.55;color:var(--ink)}
  .charm__link{position:absolute;left:14px;right:10px;bottom:18px;background:var(--pink);color:var(--white);font-size:14px;font-weight:700;border-radius:4px;padding:6px 8px;line-height:1.4}

  .session{position:absolute;left:28px;top:952px;width:792px;height:215px;background:var(--white);border-radius:6px}
  .session__brand{position:absolute;left:30px;top:22px;display:flex;align-items:center;gap:12px;color:var(--green);font-size:36px;font-weight:800}
  .session__dot{width:44px;height:44px;border-radius:50%;background:var(--green)}
  .session__title{position:absolute;left:70px;top:82px;width:230px;padding:8px 0;background:var(--pink-soft);border:3px solid var(--green);color:var(--green);font-size:30px;font-weight:800;text-align:center;line-height:1.2}
  .session__meta{position:absolute;left:340px;top:82px;font-size:22px;font-weight:700;color:var(--title);line-height:2}
  .session__online{position:absolute;left:640px;top:-8px;width:150px;padding:8px 0;background:var(--accent-blue);color:var(--white);border-radius:24px;font-size:20px;font-weight:800;text-align:center;line-height:1.25}
</style>
</head>
<body>
<main class="flyer">
  <div class="photo photo--abbey" role="img" aria-label="海に浮かぶ修道院の写真"></div>
  <div class="photo photo--buddha" role="img" aria-label="木の根に包まれた仏像の写真"></div>
  <div class="photo photo--trulli" role="img" aria-label="とんがり屋根の家並みの写真"></div>
  <div class="photo photo--cathedral" role="img" aria-label="ゴシック様式の大聖堂の写真"></div>
  <div class="photo photo--taj" role="img" aria-label="夕暮れの白い霊廟の写真"></div>
  <div class="photo photo--temple" role="img" aria-label="石造りの仏教遺跡の写真"></div>

  <header class="headline">
    <p class="headline__lead">こだま× 海外 <small>の</small></p>
    <div class="headline__brand">
      <span class="brand-mark" aria-hidden="true"></span>
      <p class="headline__name">ポコリナクラス<small>が</small></p>
    </div>
    <p class="headline__news">新しくなります！</p>
  </header>

  <div class="plane-band" aria-hidden="true"></div>
  <section class="hero-panel">
    <p class="hero-panel__main">サブスク</p>
    <p class="hero-panel__cross">×</p>
    <p class="hero-panel__main">専用アプリ</p>
    <p class="hero-panel__sub">もっとソトの世界を<br>シルチャンスを！</p>
  </section>

  <p class="charm-label">3つの魅力</p>
  <section class="charms">
    <article class="charm">
      <span class="charm__num">1</span>
      <p class="charm__text">サブスク型サービスだから多様なコンテンツに参加し放題！</p>
      <p class="charm__link">コンテンツ一覧は裏面へ→</p>
    </article>
    <article class="charm">
      <span class="charm__num">2</span>
      <p class="charm__text">アプリを活用し、よりわかりやすく、より簡単にアクセスを！</p>
      <p class="charm__link">アプリのダウンロードはこちらから→</p>
    </article>
    <article class="charm">
      <span class="charm__num">3</span>
      <p class="charm__text">兄弟や卒業生、こだまグループ会員外も参加可能に！</p>
      <p class="charm__link">料金詳細は裏面へ→</p>
    </article>
  </section>

  <section class="session">
    <div class="session__brand"><span class="session__dot" aria-hidden="true"></span>ポコリナクラス</div>
    <p class="session__title">サービス<br>概要説明会</p>
    <p class="session__meta">日時：<br>講師：</p>
    <p class="session__online">オンライン<br>開催決定!</p>
  </section>
  <div class="photo photo--host" role="img" aria-label="説明会講師の写真"></div>
</main>
</body>
</html>
```